New Therapist Looking for Unique Fun Exciting Brochure for Private Practice

I need a basic brochure displaying my services for my new therapy/counseling business. My company is Fern and Hollow PLLC and I would like something that looks earthy with green colors similar to my logo. I want just my logo and my name on the front. I would like a few pictures throughout that include trees and I have added them as uploads. I want it simple, playful and earthy with just my services, business details, my prices, qualifications, mission statement and maybe a quote. I am very authentic and want it to really represent me.

I offer mental health and substance abuse counseling for ages 14 and up. I also do body based work like yoga, breath and medication in my practice.

Will provide text content to winner - please use place holders for now.

Target Market(s)

Behavioral Health hospitals, psychiatrists, doctors, medical professionals, other therapists, substance use treatment centers, holistic practitioners

Industry/Entity Type

Counseling

Font styles to use
Serif

Colors
61bae0
85cae6
9bcb3c
abd037
cadf82
f68e4e
00a990
fbf289

Requirements
Must have
• An authentic feel, earthy and inviting - must include at least one tree picture that I included and my logo, must include one of my profile pictures
Nice to have
• Open - maybe greens and earthy tones similar to my logo
Should not have
• open

```html
<!DOCTYPE html>
<html lang="en">
<head>
<meta charset="utf-8">
<title>Fern and Hollow PLLC — Our Services</title>
<link rel="stylesheet" href="https://fonts.googleapis.com/css2?family=Roboto+Condensed:wght@300;400;700&family=Raleway:wght@400;700&family=Libre+Baskerville&display=swap">
<style>
  :root{
    --forest:#2f7a3a;
    --forest-deep:#1f5a2a;
    --sky:#7fd0e6;
    --sky-light:#a9e2ef;
    --ink:#222;
    --quote-ink:#333;
    --paper:#fff;
    --leaf-text:#3a7d3b;
    --teal:#00a990;
  }
  *{margin:0;padding:0;box-sizing:border-box}
  html,body{width:1200px;height:777px;overflow:hidden;background:var(--paper)}
  .spread{position:relative;width:1200px;height:777px;overflow:hidden;font-family:"Roboto Condensed",sans-serif;color:var(--ink)}

  .services-panel{position:absolute;left:0;top:0;width:298px;height:777px;
    background:linear-gradient(180deg,#3f8d3f 0%,var(--forest) 45%,var(--forest-deep) 100%);color:#fff}
  .services-title{position:absolute;left:42px;top:50px;font-weight:300;font-size:36px;letter-spacing:.3px}
  .specialties-label{position:absolute;left:63px;top:104px;font-weight:700;font-size:17px}
  .specialties{position:absolute;left:63px;top:136px;width:192px;list-style:none}
  .specialties li{font-weight:300;font-size:18px;height:34px;line-height:28px;border-bottom:1px solid rgba(255,255,255,.55)}
  .panel-copy{position:absolute;left:40px;width:236px;font-size:13.2px;line-height:16.5px;text-align:justify;hyphens:auto}
  .panel-copy.first{top:270px}
  .panel-copy.second{top:402px}
  .issues-label{position:absolute;left:43px;top:598px;font-weight:700;font-size:13.5px}
  .issues{position:absolute;top:632px;list-style:none;font-size:11.2px;line-height:14.1px}
  .issues.col-a{left:43px}
  .issues.col-b{left:166px}

  .forest-photo{position:absolute;left:298px;top:0;width:302px;height:777px;
    background:linear-gradient(180deg,#8fb9a0 0%,#4c7a3a 30%,#3b6a2c 60%,#5a7f36 100%)}

  .quote-panel{position:absolute;left:600px;top:0;width:600px;height:404px;
    background:linear-gradient(135deg,var(--sky-light) 0%,var(--sky) 55%,#6cc6e0 100%)}
  .quote-mark{position:absolute;left:1019px;top:82px;font-family:"Libre Baskerville",serif;font-size:44px;line-height:1;color:#111}
  .quote-text{position:absolute;left:961px;top:118px;width:144px;text-align:center;font-family:Raleway,sans-serif;font-size:11.3px;line-height:18px;color:var(--quote-ink)}
  .quote-text strong{font-weight:700;color:#111}
  .quote-author{position:absolute;left:933px;top:272px;width:200px;text-align:center;font-family:"Libre Baskerville",serif;font-size:7.6px;letter-spacing:1px;text-transform:uppercase;color:var(--quote-ink)}
  .quote-source{position:absolute;left:933px;top:306px;width:200px;text-align:center;font-family:"Libre Baskerville",serif;font-size:6px;color:var(--quote-ink)}

  .room-frame{position:absolute;left:461px;top:42px;width:416px;height:310px;background:var(--paper)}
  .room-photo{position:absolute;left:22px;top:15px;width:370px;height:277px;
    background:linear-gradient(180deg,#d8d8d6 0%,#bdbcb8 60%,#5a5c60 80%,#3f4145 100%)}

  .brand-mark{position:absolute;left:640px;top:478px;width:160px;display:flex;flex-direction:column;align-items:center;gap:12px}
  .brand-circle{width:64px;height:64px;border-radius:50%;background:var(--teal)}
  .brand-name{font-size:16px;font-weight:400;color:var(--leaf-text);text-align:center;line-height:19px}

  .about-copy{position:absolute;left:813px;width:340px;font-size:12.9px;line-height:16.5px;text-align:justify;hyphens:auto}
  .about-copy.first{top:426px}
  .about-copy.second{top:524px}
  .clientele{position:absolute;left:817px;top:666px;width:355px;font-size:17px;line-height:21px;color:var(--leaf-text);text-align:justify}
</style>
</head>
<body>
<main class="spread">
  <section class="services-panel" role="img" aria-label="Pine forest photograph under a green tint">
    <h1 class="services-title">Our Services</h1>
    <h2 class="specialties-label">Specialties</h2>
    <ul class="specialties">
      <li>Relationship Issues</li>
      <li>Mood Disorders</li>
      <li>Self Esteem</li>
    </ul>
    <p class="panel-copy first">I enjoy working with clients who want to improve the quality of their relationships. As part of supporting clients in addressing relationship issues, my work can involve working with clients on individual issues such as reducing depression and anxiety.</p>
    <p class="panel-copy second">I assist clients in exploring and processing feelings that contribute to depression and anxiety with the goal of promoting individual well-being which, in turn, contributes to improvement in relationships. I utilize a collaborative approach that involves supporting clients in understanding how past life experiences and current life issues are impacting their lives. Connecting clients with strengths is a primary treatment goal.</p>
    <h2 class="issues-label">Issues</h2>
    <ul class="issues col-a">
      <li>Addiction</li><li>Alcohol Use</li><li>Anger Management</li><li>Anxiety</li><li>Child or Adolescent</li><li>Coping Skills</li><li>Depression</li>
    </ul>
    <ul class="issues col-b">
      <li>Drug Abuse</li><li>Family Conflict</li><li>Grief</li><li>Parenting</li><li>Peer Relationships</li><li>School Issues</li><li>Substance Use</li>
    </ul>
  </section>

  <div class="forest-photo" role="img" aria-label="Photograph of tall trees in a sunlit forest"></div>

  <section class="quote-panel"></section>
  <div class="quote-mark">&ldquo;</div>
  <p class="quote-text">The reality of our work is that in order to sustain and enjoy it, we must intentionally deal with the nuances of what it means to function as a therapist <strong>inside and outside</strong> the therapy room.</p>
  <p class="quote-author">Mara Lindqvist, PhD</p>
  <p class="quote-source">©2018, on MindCraft Journal</p>

  <div class="room-frame">
    <div class="room-photo" role="img" aria-label="Photograph of the counseling room with a sofa, armchair, coffee table and bookshelf"></div>
  </div>

  <div class="brand-mark">
    <span class="brand-circle"></span>
    <span class="brand-name">Fern and Hollow PLLC</span>
  </div>

  <p class="about-copy first">I enjoy working with clients who want to improve the quality of their relationships. As part of supporting clients in addressing relationship issues, my work can involve working with clients on individual issues such as reducing depression and anxiety.</p>
  <p class="about-copy second">I assist clients in exploring and processing feelings that contribute to depression and anxiety with the goal of promoting individual well-being which, in turn, contributes to improvement in relationships. I utilize a collaborative approach that involves supporting clients in understanding how past life experiences and current life issues are impacting their lives. Connecting clients with strengths is a primary treatment goal.</p>
  <p class="clientele">I work with individuals, couples, families, children, teens, and seniors. I have experience addressing substance use, gender, and HIV/AIDS issues.</p>
</main>
</body>
</html>
```